Green Logistics / Last Mile Delivery Firm needs cool one-page website

FYI - We do have a detailed brief in the uploaded files section below
COMPANY
We recently launched the company Brook Logistics which is a pioneer in urban green logistics and provides zero-emissions last mile delivery services (i.e. delivery of parcels with delivery vans to the doorstep of households) for its logistics and retail clients.
We take on urban parcel delivery for our clients with a 100% electric commercial vehicles fleet, fair and sustainable working conditions for our employees and an unparalleled professional and customer-focused mindset.
WEBSITE
In the detailed brief, we have provided examples to emulate. We need the design + coding of the website. Website needs to be friendly/optimized for and should open swiftly on both Android & iOS.
In general, the website should convey
- green mission of the company
- sustainability (good working conditions, focus on employees)
- customer orientation
- professionalism
DESIGN
In the detailed brief, we have provided designs to emulate.
Color design: we do have a logo which features 2 green colors (one lighter and one darker color tone). However, the colors on the website do not necessarily need to follow these 2 colors exactly as we are able to switch the logo colors.
Imagery: should reflect maybe 50% green/leaf/tree , 25% customer and employee orientation, and 25% logistics (here it's important that it is the last mile delivery, i.e. delivery with delivery vans to the doorstep of households)
Coding

```html
<!DOCTYPE html>
<html lang="en">
<head>
<meta charset="utf-8">
<title>Brook Logistics – Delivering Parcels Emissions-Free</title>
<link href="https://fonts.googleapis.com/css2?family=Poppins:wght@300;400;500;600;700;800&family=Lato:wght@400;700&display=swap" rel="stylesheet">
<style>
:root{
  --green:#1a9442;
  --green-dark:#137a35;
  --lime:#8cc63f;
  --lime-light:#a9d65a;
  --ink:#1e1e1e;
  --text:#3a3a3a;
  --muted:#6b6b6b;
  --paper:#ffffff;
  --mist:#f3f3f3;
  --line:#cfcfcf;
}
*{margin:0;padding:0;box-sizing:border-box}
html,body{width:1200px;height:3599px;overflow:hidden}
body{font-family:"Poppins",sans-serif;color:var(--text);background:var(--paper);position:relative}
section,header,footer{position:absolute;left:0;width:1200px}
.abs{position:absolute}
.btn{position:absolute;background:var(--green);color:#fff;font-family:"Lato",sans-serif;font-weight:700;font-size:11px;display:flex;align-items:center;justify-content:center;border-radius:2px;box-shadow:0 2px 4px rgba(0,0,0,.2)}
.heading{font-weight:800;color:var(--green);letter-spacing:-.5px}
.body-copy{font-size:10.5px;line-height:18px;color:var(--text)}
.body-copy p+p{margin-top:14px}

/* nav */
.site-header{top:0;height:50px;background:#fff;box-shadow:0 1px 4px rgba(0,0,0,.15);z-index:3}
.brand{left:249px;top:12px;display:flex;align-items:center;gap:8px;font-weight:600;font-size:13px;color:var(--green)}
.brand-dot{width:26px;height:26px;border-radius:50%;background:var(--lime)}
.main-nav{left:622px;top:18px;display:flex;gap:18px;font-family:"Lato",sans-serif;font-size:11px;color:var(--ink)}
.lang{left:879px;top:13px;width:72px;height:25px;font-size:11px}

/* hero */
.hero{top:50px;height:506px;background:radial-gradient(ellipse at 50% 45%,#2c3a2e 0%,#1a241c 55%,#0d140f 100%)}
.hero-title{top:196px;width:100%;text-align:center;color:#fff;font-weight:800;font-size:31px;letter-spacing:-.5px}
.hero-sub{top:240px;width:100%;text-align:center;color:#fff;font-weight:300;font-size:37px}
.hero .btn{left:546px;top:316px;width:108px;height:32px}

/* who */
.who{top:556px;height:455px;background:linear-gradient(90deg,#f1f1f1,#fafafa 60%,#f3f3f3)}
.who-card{left:249px;top:91px;width:360px;height:267px;background:var(--mist);box-shadow:0 2px 10px rgba(0,0,0,.12);padding:34px 37px}
.who-card .heading{font-size:22px;margin-bottom:16px}
.who-photo{left:612px;top:61px;width:339px;height:333px;background:linear-gradient(135deg,#c9d6e0,#e8e3da 50%,#8a98a8);box-shadow:0 4px 12px rgba(0,0,0,.2)}

/* mission */
.mission{top:1011px;height:256px;background:var(--green);color:#fff;text-align:center}
.mission h2{position:absolute;top:50px;width:100%;font-size:22px;font-weight:800;letter-spacing:-.5px}
.mission p{position:absolute;left:300px;top:96px;width:600px;font-size:15px;line-height:23px}

/* values */
.values{top:1267px;height:467px;background:linear-gradient(90deg,#f6f6f6,#f0f0f0)}
.values-photo{left:250px;top:62px;width:337px;height:331px;background:radial-gradient(ellipse at 50% 45%,#6aa32a,#2f5a14 55%,#0f1e08);box-shadow:0 4px 12px rgba(0,0,0,.25)}
.values-card{left:587px;top:92px;width:364px;height:266px;background:#fff;box-shadow:0 2px 10px rgba(0,0,0,.1);padding:34px 34px}
.values-card .heading{font-size:22px;margin-bottom:14px}

/* services */
.services{top:1734px;height:417px;background:#fff}
.services h2{position:absolute;top:42px;width:100%;text-align:center;font-size:28px}
.svc{top:113px;width:216px;height:237px;background:#fff;box-shadow:0 2px 10px rgba(0,0,0,.15);text-align:center;padding:0 8px}
.svc-icon{width:110px;height:100px;margin:36px auto 16px;border-radius:6px;background:linear-gradient(135deg,#e4f3e8,#c6e6cf)}
.svc h3{font-size:11.5px;font-weight:600;color:var(--ink);margin-bottom:6px;white-space:nowrap}
.svc p{font-size:9px;line-height:15px;color:var(--text);padding:0 12px}
.arrow{top:212px}

/* touch */
.touch{top:2151px;height:336px;background:radial-gradient(ellipse at 50% 40%,#3a3f44,#1b1e21 70%,#0f1113);color:#fff;text-align:center}
.touch h2{position:absolute;top:82px;width:100%;font-size:29px;font-weight:800;letter-spacing:-.5px}
.touch p{position:absolute;left:325px;top:136px;width:550px;font-size:14px;line-height:24px}
.touch .btn{left:560px;top:224px;width:106px;height:32px}

/* careers */
.careers{top:2487px;height:437px;background:#fff}
.careers-photo{left:0;top:0;width:601px;height:437px;background:linear-gradient(135deg,#d9d4cf,#7f7b78 45%,#2a2b30)}
.careers-copy{left:666px;top:36px;width:440px}
.careers-copy .heading{font-size:22px;margin-bottom:16px}
.careers .btn{left:666px;top:359px;width:108px;height:33px}

/* contact */
.contact{top:2924px;height:370px;background:linear-gradient(90deg,#f7f7f7,#fdfdfd)}
.info{left:249px;display:flex;gap:12px}
.info svg{flex:none;margin-top:2px}
.info b{display:block;font-size:12px;color:var(--green);font-weight:600}
.info span{font-size:12px;color:var(--ink)}
.field{position:absolute;border:1px solid var(--line);background:#fff;font-size:9px;color:var(--muted);padding:8px 14px}
.contact .btn{left:552px;top:264px;width:106px;height:33px}

/* footer */
.site-footer{top:3294px;height:305px;background:linear-gradient(160deg,var(--lime) 0%,var(--lime-light) 50%,var(--lime) 100%);color:#fff}
.footer-mark{left:518px;top:-54px;width:140px;height:140px;border-radius:50%;background:#fff}
.footer-name{top:108px;width:100%;text-align:center;font-weight:600;font-size:32px}
.socials{left:528px;top:181px;display:flex;gap:9px}
.socials span{width:30px;height:30px;border-radius:50%;border:2px solid #fff}
.footer-nav{top:232px;width:100%;display:flex;justify-content:center;gap:22px;font-size:13px}
.copy{left:249px;top:278px;font-size:9px}
.legal{right:249px;top:278px;font-size:10px}
</style>
</head>
<body>

<header class="site-header">
  <div class="abs brand"><span class="brand-dot"></span>Brook Logistics</div>
  <nav class="abs main-nav"><span>Home</span><span>About</span><span>Services</span><span>Careers</span><span>Contact</span></nav>
  <div class="btn lang">English ▾</div>
</header>

<section class="hero" role="img" aria-label="Dark green tropical leaves background">
  <h1 class="abs hero-title">DELIVERING PARCELS EMISSIONS-FREE</h1>
  <p class="abs hero-sub">Because we care about trees!</p>
  <div class="btn">Get started</div>
</section>

<section class="who">
  <div class="abs who-card">
    <h2 class="heading">WHO WE ARE</h2>
    <div class="body-copy">
      <p>Brook Logistics is a pioneer in urban green logistics and provides zero-emissions last mile delivery services for its logistics and retail clients.</p>
      <p>We take on urban parcel delivery for our clients with a 100% electric commercial vehicles fleet, fair and sustainable working conditions for our employees and an unparalleled professional and customer-focused mindset.</p>
    </div>
  </div>
  <div class="abs who-photo" role="img" aria-label="Photo of a smiling team working together at a laptop"></div>
</section>

<section class="mission">
  <h2>OUR MISSION</h2>
  <p>To satisfy consumers' ever-rising desire to buy products online, the CO2 emissions from delivery traffic will increase by 32% in the top 100 cities globally until 2030. Our clients care about our planet the same way we do, which is why Brook Logistics helps to make the planet a better place by running the most environmentally friendly urban last mile possible.</p>
</section>

<section class="values">
  <div class="abs values-photo" role="img" aria-label="Close-up photo of green moss"></div>
  <div class="abs values-card">
    <h2 class="heading">OUR VALUES</h2>
    <div class="body-copy">
      <p>We see ourselves as a professional services company who strongly cares about the environment, its clients and their customers, as well as its employees.</p>
      <p>We believe that delivering parcels with zero emissions and providing a unique customer experience through a highly professional attitude and a great team spirit are the cornerstones for Brook Logistics to operate in today's world in a sustainable yet profitable way.</p>
    </div>
  </div>
</section>

<section class="services">
  <h2 class="heading">SERVICES</h2>
  <svg class="abs arrow" style="left:208px" width="20" height="30" viewBox="0 0 20 30"><path d="M15 3 4 15l11 12" fill="none" stroke="#111" stroke-width="3"/></svg>
  <div class="abs svc" style="left:250px">
    <div class="svc-icon" role="img" aria-label="Electric delivery van icon"></div>
    <h3>Zero-emission delivery</h3>
    <p>We operate a 100% electric commercial vehicle fleet</p>
  </div>
  <div class="abs svc" style="left:492px">
    <div class="svc-icon" role="img" aria-label="Delivery driver with clipboard icon"></div>
    <h3>Highly trained delivery drivers</h3>
    <p>We only employ permanently, train far above average, and live a great team spirit</p>
  </div>
  <div class="abs svc" style="left:735px">
    <div class="svc-icon" role="img" aria-label="Shield with professional icon"></div>
    <h3>Professional all around</h3>
    <p>We honor our commitments and hold ourselves to the highest professional standards</p>
  </div>
  <svg class="abs arrow" style="left:975px" width="20" height="30" viewBox="0 0 20 30"><path d="M5 3l11 12L5 27" fill="none" stroke="#111" stroke-width="3"/></svg>
</section>

<section class="touch" role="img" aria-label="Dark photo of hands typing on a keyboard">
  <h2>GET IN TOUCH WITH BROOK LOGISTICS</h2>
  <p>If you got excited, or have a question about our services, our approach, our jobs or just want to get in touch to chat about how green logistics can make the planet a little bit better, please get in touch!</p>
  <div class="btn">Contact us</div>
</section>

<section class="careers">
  <div class="abs careers-photo" role="img" aria-label="Photo of business people shaking hands with thumbs up"></div>
  <div class="abs careers-copy">
    <h2 class="heading">CAREERS</h2>
    <div class="body-copy">
      <p>If you join Brook Logistics, you join a family. We elevate one another, care for each other's wellbeing and growth, and celebrate our successes. We strongly believe growth is a team sport and that every member of the family fully contributes to the achievements of the company overall.</p>
      <p>At the heart of everything we do at Brook Logistics is a relentless focus on our mission. That's why we aim to ensure our employees can follow their own passion at the workplace, be this working in a truly collaborative and caring team, putting a smile on a customer's face or making the world a better place.</p>
      <p>While we are helping our clients grow by delivering their parcels, we are also helping all our employees grow personally and professionally. We care about our employees' happiness and wellbeing which is why we provide additional benefits like supplementary health insurance.</p>
    </div>
  </div>
  <div class="btn">Read More</div>
</section>

<section class="contact">
  <div class="abs info" style="top:48px">
    <svg width="16" height="20" viewBox="0 0 16 20"><path d="M8 0a7 7 0 0 0-7 7c0 5 7 13 7 13s7-8 7-13a7 7 0 0 0-7-7z" fill="#1a9442"/><circle cx="8" cy="7" r="2.6" fill="#fff"/></svg>
    <div><b>Location:</b><span>12 Fern Lane, Greenfield, AB 56982</span></div>
  </div>
  <div class="abs info" style="top:105px">
    <svg width="18" height="14" viewBox="0 0 18 14"><rect x="0" y="0" width="18" height="14" rx="1" fill="#1a9442"/><path d="M1 1l8 7 8-7M1 13l6-6M17 13l-6-6" fill="none" stroke="#fff" stroke-width="1.4"/></svg>
    <div><b>Email:</b><span>info@brooklogistics.com</span></div>
  </div>
  <div class="abs info" style="top:165px">
    <svg width="18" height="18" viewBox="0 0 18 18"><path d="M4 1l3 4-2 2c1 3 3 5 6 6l2-2 4 3-2 3C8 17 1 10 1 3z" fill="#1a9442"/></svg>
    <div><b>Call:</b><span>+1 23 555 01789</span></div>
  </div>
  <div class="field" style="left:552px;top:44px;width:189px;height:31px">Your Name</div>
  <div class="field" style="left:761px;top:44px;width:190px;height:31px">Email</div>
  <div class="field" style="left:552px;top:96px;width:399px;height:31px">Subject</div>
  <div class="field" style="left:552px;top:148px;width:399px;height:97px">Message</div>
  <div class="btn">Submit</div>
</section>

<footer class="site-footer">
  <div class="abs footer-mark"></div>
  <div class="abs footer-name">Brook Logistics</div>
  <div class="abs socials" aria-label="Social links"><span></span><span></span><span></span></div>
  <nav class="abs footer-nav"><span>Home</span><span>About</span><span>Services</span><span>Careers</span><span>Contact</span></nav>
  <div class="abs copy">© 2020 Brook Logistics</div>
  <div class="abs legal">Legal Notice &nbsp;|&nbsp; Privacy Policy</div>
</footer>

</body>
</html>
```